Create the BEST and COOLEST website for events and media company!

Hi there. I am a start-up events and conferences company with a twist, and we are seeking a highly modern website for our company Lumen Harbor Media. Our company believes that (like the social networking theory) that each and every one of us is connected to anyone on the planet in six connections or less. E.g. I know someone, who knows someone, who knows someone. Hence, the name Lumen Harbor Media.

I have included the copy for the website attached.

While we do have a business audience, they are in the fields of technology from the banking, health, government sector. We would like our website to be edgy, fresh and steer away from stuffy corporate images.

To give you an idea, our website menu tabs will be labelled:
HOME: This will include a corporate video that’s being created next week for me. However, please still design this page with a very striking background image that fills the whole page. You can run the copy and put a mock video for me to just see the layout (we can insert the finished video later).

ROCKSTARS: this will show pictures of highly powerful leaders speaking on stage; with a highly engaged audience watching. We want to show we have the world’s best technology International speakers “rockstars” who are the best in their game when it comes to talking about the future of technology.

LOCAL LEGENDS: like the international ‘rockstar’ speakers we would bring over to Australia to present; this LOCAL LEGENDS page should show we have the best home-grown Chief business people speaking at conferences and smaller powerful roundtable luncheons.

UNSUNG HEROES: this is more the people in the audience who ask questions on a microphone; those that attend the conferences; or a speaking to people at a conference.

THE BAND: this is like an ‘about us’ – just a funkier name to tie in with the theme of rockstars, etc.

THE PARTNERS: this is like a sponsor client page, where we invite people to partner with us and sponsor our events and conferences.

YOU & DORIAN FLECK: Dorian Fleck is a famous actor who made the term ‘six degrees of separation’ very popular. This page will have a little bit of an introduction, but mainly have the following video fill the landing page: https://www.vidstreamhub.example/watch?v=Qzt-plK4WB8

Website Functionality and Features:

• Try and make the ‘vibe’ and look and feel consistent, hip and modern (but still maintain a professional look). At the end of the day, people looking at our website are very senior business chiefs of organisations and also marketing chiefs.
• We may add more pages once we become established, so the website needs to ensure we can do that easily.
• We want pictures to not look stock photos. We want them to fresh, innovative, inspirational.
• Images should have a ‘wow’ factor. Like this one: https://www.stockframebank.example/detail/news-photo/general-view-of-crowd-during-brightloop-talks-2018-news-photo/481203967
• Need a mix of speaker, stage, audience, pictures. While we want to be fresh, edgy and contemporary we need to remember our viewers are the big chiefs of businesses – so lets try and have cool shots, but ensure there is a link to the business decision makers in a modern way. They all don’t have to wear suits, but not too casual either
• Other types of imagery I like is this one: https://www.stockframebank.example/detail/photo/smiling-audience-using-smart-phone-flashlights-for-royalty-free-image/372815094.
• The following are ok, not wow – but to give you an idea:
• https://www.stockframebank.example/detail/photo/smiling-male-speaker-in-wheelchair-on-stage-royalty-free-image/372816288
https://www.stockframebank.example/detail/photo/smiling-woman-with-camera-phone-in-dark-audience-royalty-free-image/372817452
https://www.stockframebank.example/detail/photo/audience-using-camera-phones-royalty-free-image/376630581
https://www.stockframebank.example/detail/photo/male-speaker-on-stage-talking-to-audience-royalty-free-image/372818736

NB: Logos are supplied in low resolution, but I can send you high resolution also
Updates

Hi there I will be adding two low-resolution images of my business partner and I for the ABOUT US page which is called THE BAND in the menu tab.

Hi everyone, thank you for your designs. I have uploaded a MAIN SCREEN IDEAS word document to give you further ideas of how the options I like for the main landing page on the home page. Hope this helps!

Target Market(s)

High end business people in marketing and business.

Coding

Coded - Design and coding required

Number of Pages Required

5+ page

Font styles to use
Sans Serif

Requirements
Must have
• Fresh, inspirational and aspirational designs. We need to make events and conferences look exciting and that we are bring the best technology speakers (like BrightLoop events) to our audience of marketing and technology professionals.
Should not have
• Cheesy, old stock photos; or pictures of American executives as this is for an Australian audience.
• PLEASE do not include an UPCOMING EVENTS or a SPEAKERS section as we will not be having this showcasing. You can feature ROCK STARS, LOCAL LEGENDS and UNSUNG HEROES if you like on the home page + the video of YOU and DORIAN FLECK (with his picture on the video box with a play button)

```html
<!DOCTYPE html>
<html lang="en">
<head>
<meta charset="utf-8">
<title>Lumen Harbor Media</title>
<link href="https://fonts.googleapis.com/css2?family=Roboto:wght@300;400;500;700&display=swap" rel="stylesheet">
<style>
:root{
  --orange:#ff8a1e;
  --teal:#1ec9b0;
  --ink:#1d1d1d;
  --muted:#8a8a8a;
  --icon:#b9b9b9;
  --line:#dcdcdc;
  --soft:#f4f4f4;
  --white:#ffffff;
}
*{box-sizing:border-box;margin:0;padding:0}
html,body{width:1200px;height:3509px;overflow:hidden}
body{position:relative;font-family:'Roboto',Arial,sans-serif;color:var(--ink);background:var(--white)}
a{color:inherit;text-decoration:none}
.abs{position:absolute}
.section-title{position:absolute;left:0;width:1200px;text-align:center;font-weight:700;font-size:20px;letter-spacing:.5px}
.section-title::after{content:"";display:block;width:28px;height:3px;background:var(--teal);margin:10px auto 0}
.section-title--plain::after{display:none}
.section-title--light{color:var(--white)}
.section-title--light::after{background:var(--white)}
.lede{position:absolute;left:330px;width:540px;text-align:center;font-size:11px;line-height:19px;color:var(--muted)}
.lede--light{color:var(--white)}

/* social links */
.social{display:flex;gap:10px;align-items:center}
.social a{display:block;width:12px;height:12px;color:var(--icon)}
.social a.is-active{color:var(--orange)}
.social svg{width:12px;height:12px;display:block;fill:none;stroke:currentColor;stroke-width:2;stroke-linecap:round;stroke-linejoin:round}

/* hero */
.hero{top:0;left:0;width:1200px;height:601px;background:radial-gradient(circle at 58% 30%,#9a7a66 0,#5b4536 30%,#2d2620 70%,#1b1715 100%)}
.hero-photo{position:absolute;inset:0}
.brand{position:absolute;top:0;left:159px;width:161px;height:89px;background:var(--white);display:flex;align-items:center;justify-content:center;box-shadow:0 3px 10px rgba(0,0,0,.3)}
.brand span{color:var(--orange);font-weight:700;font-size:15px;line-height:18px;text-align:center}
.nav{position:absolute;top:0;left:426px;display:flex;height:58px}
.nav a{color:var(--white);font-size:12px;font-weight:500;padding:0 11px;line-height:58px}
.nav a.active{background:var(--white);color:var(--orange)}
.play{position:absolute;border:3px solid var(--white);border-radius:50%}
.play::after{content:"";position:absolute;border-left-color:var(--white);border-left-style:solid;border-top:solid transparent;border-bottom:solid transparent}
.play--hero{left:564px;top:263px;width:72px;height:72px}
.play--hero::after{left:27px;top:19px;border-left-width:22px;border-top-width:14px;border-bottom-width:14px}
.play--video{left:714px;top:2253px;width:56px;height:56px}
.play--video::after{left:21px;top:14px;border-left-width:17px;border-top-width:11px;border-bottom-width:11px}

/* rockstars */
.rock-title{top:652px;font-size:23px}
.rock-lede{top:694px;left:230px;width:740px}
.speaker-photo{position:absolute;width:126px;height:126px;border:6px solid #eeeeee;background:linear-gradient(#e9e9e9,#bdbdbd)}
.speaker-text{position:absolute;width:240px;font-size:10px;line-height:17px;color:var(--muted)}
.speaker-text h4{font-size:13px;color:var(--ink);margin-bottom:6px}
.speaker-text em{display:block;margin-bottom:6px}
.speaker-text--right{text-align:right}
.speaker-text--right .social{justify-content:flex-end}
.speaker-text .social{margin-top:10px}
.btn-more{position:absolute;left:554px;top:1153px;width:89px;height:25px;border:1px solid var(--orange);color:var(--orange);font-size:9px;text-align:center;line-height:23px;font-weight:500}

/* local legends */
.legends-intro{top:1240px;left:0;width:437px;height:300px;background:var(--orange);color:var(--white);padding:55px 0 0 161px}
.legends-intro h2{font-size:19px;font-weight:700}
.legends-intro h2::after{content:"";display:block;width:28px;height:3px;background:var(--white);margin:12px 0 18px}
.legends-intro p{font-size:10px;line-height:18px;width:210px}
.legends-stage{top:1240px;left:437px;width:763px;height:300px;background:linear-gradient(100deg,#2a2c2e,#121314 60%,#1e1f21)}
.legend{position:absolute;top:65px;width:160px;text-align:center;color:var(--white)}
.legend .avatar{width:94px;height:94px;border-radius:50%;border:5px solid #3a3b3d;margin:0 auto;background:linear-gradient(#b99a86,#5b4a40)}
.legend h4{font-size:13px;margin-top:16px}
.legend em{display:block;font-size:10px;color:var(--teal);margin:5px 0 8px}
.legend .social{justify-content:center}
.legend .social a{color:#ececec}
.legend .social a.is-active{color:var(--orange)}
.pager{position:absolute;top:217px;width:23px;height:23px;border:1px solid var(--white);display:flex;align-items:center;justify-content:center}
.pager--on{background:var(--orange);border-color:var(--orange)}

/* unsung heroes */
.heroes-title{top:1597px}
.heroes-clip{position:absolute;top:1540px;left:0;width:1200px;height:455px;overflow:hidden}
.arc{top:132px;left:285px;width:632px;height:632px;border-radius:50%;background:linear-gradient(#0d0d0d,#222)}
.hero-card{position:absolute;top:1743px;width:128px;height:194px;background:var(--white);box-shadow:0 4px 14px rgba(0,0,0,.2);padding:6px;text-align:center}
.hero-card .pic{height:126px;background:linear-gradient(#dcdcdc,#9a9a9a)}
.hero-card h5{font-size:11px;margin-top:10px}
.hero-card small{font-size:9px;color:var(--muted)}
.hero-card--featured{background:var(--orange);color:var(--white)}
.hero-card--featured small{color:var(--white)}
.mic{position:absolute;top:-12px;left:52px;width:24px;height:24px;border-radius:50%;background:var(--teal)}
.mic::after{content:"";position:absolute;left:9px;top:5px;width:6px;height:10px;border-radius:3px;background:var(--white)}
.arrow{position:absolute;top:1826px;font-size:22px;color:#9a9a9a}
.arrow--next{color:var(--orange)}

/* you & dorian */
.dorian{top:1995px;left:0;width:1200px;height:501px;background:var(--soft)}
.dorian-title{top:2052px}
.dorian-head{position:absolute;left:161px;top:2132px;width:270px;font-size:19px;font-weight:700;line-height:26px}
.dorian-copy{position:absolute;left:161px;top:2290px;width:265px;font-size:10px;line-height:18px;color:var(--muted)}
.video{top:2126px;left:461px;width:578px;height:309px;border-radius:4px;background:radial-gradient(circle at 45% 40%,#7a7a7a,#2c2c2c 60%,#111)}

/* partners */
.partner-title{top:2550px}
.partner-lede{top:2609px}
.partner{position:absolute;top:2685px;width:126px;height:84px;border:5px solid #e3e3e3;display:flex;align-items:center;justify-content:center;font-size:12px;color:#555}
.nav-btn{position:absolute;top:2702px;width:23px;height:52px;display:flex;align-items:center;justify-content:center}
.nav-btn--prev{left:161px;background:var(--orange)}
.nav-btn--next{left:1016px;border:1px solid var(--line)}

/* contact */
.contact{top:2830px;left:0;width:1200px;height:405px;background:var(--orange)}
.contact-title{top:2886px}
.contact-lede{top:2946px}
.field{position:absolute;left:161px;width:426px;height:28px;border:1px solid rgba(255,255,255,.8);color:var(--white);font-size:10px;padding:7px 8px}
.field--message{left:610px;width:429px;height:103px}
.send{position:absolute;left:161px;top:3141px;width:878px;height:33px;background:var(--white);color:var(--ink);font-size:10px;text-align:center;line-height:33px;border-radius:2px}

/* connect */
.connect-title{top:3290px;font-size:24px;font-weight:500}
.connect-sub{top:3330px;left:0;width:1200px;text-align:center;font-size:14px;color:#666;letter-spacing:.5px}
.follow{top:3370px;left:510px;display:flex;gap:21px}
.follow a{width:38px;height:38px;border-radius:50%;background:var(--orange);display:flex;align-items:center;justify-content:center;color:var(--white)}
.follow svg{width:18px;height:18px;fill:none;stroke:currentColor;stroke-width:2;stroke-linecap:round;stroke-linejoin:round}
.copyright{top:3437px;left:0;width:1200px;text-align:center;font-size:10px;color:var(--muted)}
</style>
</head>
<body>

<svg width="0" height="0" style="position:absolute" aria-hidden="true">
  <defs>
    <symbol id="i-share" viewBox="0 0 24 24"><circle cx="18" cy="5" r="3"/><circle cx="6" cy="12" r="3"/><circle cx="18" cy="19" r="3"/><path d="M8.6 13.5l6.8 4M15.4 6.5l-6.8 4"/></symbol>
    <symbol id="i-link" viewBox="0 0 24 24"><path d="M10 14a5 5 0 0 0 7 0l3-3a5 5 0 0 0-7-7l-1 1"/><path d="M14 10a5 5 0 0 0-7 0l-3 3a5 5 0 0 0 7 7l1-1"/></symbol>
    <symbol id="i-mail" viewBox="0 0 24 24"><rect x="3" y="5" width="18" height="14" rx="2"/><path d="M3 7l9 6 9-6"/></symbol>
    <symbol id="i-globe" viewBox="0 0 24 24"><circle cx="12" cy="12" r="9"/><path d="M3 12h18M12 3a14 14 0 0 1 0 18M12 3a14 14 0 0 0 0 18"/></symbol>
  </defs>
</svg>

<header class="abs hero">
  <div class="hero-photo" role="img" aria-label="Conference audience member asking a question into a microphone, crowd around her"></div>
  <div class="brand"><span>Lumen Harbor<br>Media</span></div>
  <nav class="nav">
    <a href="#" class="active">Home</a><a href="#">Rockstars</a><a href="#">Local Legends</a><a href="#">Unsung Heroes</a><a href="#">The Band</a><a href="#">The Partners</a><a href="#">You &amp; Dorian Fleck</a><a href="#">Contact</a>
  </nav>
  <div class="play play--hero"></div>
</header>

<h2 class="section-title section-title--plain rock-title">World’s Best Technology International Speakers “Rock Stars”</h2>
<p class="lede rock-lede">Sed ut perspiciatis unde omnis iste natus error sit voluptatem accusantium doloremque laudantium, totam rem aperiam, eaque ipsa quae ab illo inventore veritatis et quasi architecto beatae vitae dicta sunt explicabo. Nemo enim ipsam voluptatem quia voluptas sit aspernatur aut odit aut fugit, sed quia consequuntur magni dolores eos qui ratione voluptatem sequi nesciunt.</p>

<div class="speaker-text speaker-text--right" style="left:176px;top:803px"><h4>Speaker Name</h4><em>Profession</em>Sed ut perspiciatis unde omnis iste natus error sit voluptatem accusantium doloremque
  <div class="social"><a href="#" class="is-active" aria-label="Share"><svg><use href="#i-share"/></svg></a><a href="#" aria-label="Website"><svg><use href="#i-link"/></svg></a><a href="#" aria-label="Email"><svg><use href="#i-mail"/></svg></a><a href="#" aria-label="Profile"><svg><use href="#i-globe"/></svg></a></div></div>
<div class="speaker-photo" style="left:447px;top:807px" role="img" aria-label="Speaker portrait"></div>
<div class="speaker-photo" style="left:627px;top:807px" role="img" aria-label="Speaker portrait"></div>
<div class="speaker-text" style="left:781px;top:803px"><h4>Speaker Name</h4><em>Profession</em>Sed ut perspiciatis unde omnis iste natus error sit voluptatem accusantium doloremque
  <div class="social"><a href="#" aria-label="Share"><svg><use href="#i-share"/></svg></a><a href="#" aria-label="Website"><svg><use href="#i-link"/></svg></a><a href="#" aria-label="Email"><svg><use href="#i-mail"/></svg></a><a href="#" aria-label="Profile"><svg><use href="#i-globe"/></svg></a></div></div>

<div class="speaker-text speaker-text--right" style="left:176px;top:958px"><h4>Speaker Name</h4><em>Profession</em>Sed ut perspiciatis unde omnis iste natus error sit voluptatem accusantium doloremque
  <div class="social"><a href="#" aria-label="Share"><svg><use href="#i-share"/></svg></a><a href="#" aria-label="Website"><svg><use href="#i-link"/></svg></a><a href="#" aria-label="Email"><svg><use href="#i-mail"/></svg></a><a href="#" aria-label="Profile"><svg><use href="#i-globe"/></svg></a></div></div>
<div class="speaker-photo" style="left:447px;top:962px" role="img" aria-label="Speaker portrait"></div>
<div class="speaker-photo" style="left:627px;top:962px" role="img" aria-label="Speaker portrait"></div>
<div class="speaker-text" style="left:781px;top:958px"><h4>Speaker Name</h4><em>Profession</em>Sed ut perspiciatis unde omnis iste natus error sit voluptatem accusantium doloremque
  <div class="social"><a href="#" aria-label="Share"><svg><use href="#i-share"/></svg></a><a href="#" aria-label="Website"><svg><use href="#i-link"/></svg></a><a href="#" aria-label="Email"><svg><use href="#i-mail"/></svg></a><a href="#" aria-label="Profile"><svg><use href="#i-globe"/></svg></a></div></div>

<a href="#" class="btn-more">SEE MORE</a>

<section class="abs legends-intro">
  <h2>LOCAL LEGENDS</h2>
  <p>Nemo enim ipsam voluptatem quia voluptas sit aspernatur aut odit aut fugit, sed quia consequuntur magni dolores eos qui ratione voluptatem sequi nesciunt. Neque porro quisquam est, qui dolorem ipsum quia dolor sit amet, consectetur, adipisci velit.</p>
</section>
<section class="abs legends-stage" role="img" aria-label="Dim conference room with a roundtable audience">
  <div class="legend" style="left:73px"><div class="avatar"></div><h4>Speaker Name</h4><em>Profession</em>
    <div class="social"><a href="#" class="is-active" aria-label="Share"><svg><use href="#i-share"/></svg></a><a href="#" aria-label="Website"><svg><use href="#i-link"/></svg></a><a href="#" aria-label="Email"><svg><use href="#i-mail"/></svg></a><a href="#" aria-label="Profile"><svg><use href="#i-globe"/></svg></a></div></div>
  <div class="legend" style="left:260px"><div class="avatar"></div><h4>Speaker Name</h4><em>Profession</em>
    <div class="social"><a href="#" aria-label="Share"><svg><use href="#i-share"/></svg></a><a href="#" aria-label="Website"><svg><use href="#i-link"/></svg></a><a href="#" aria-label="Email"><svg><use href="#i-mail"/></svg></a><a href="#" aria-label="Profile"><svg><use href="#i-globe"/></svg></a></div></div>
  <div class="legend" style="left:442px"><div class="avatar"></div><h4>Speaker Name</h4><em>Profession</em>
    <div class="social"><a href="#" aria-label="Share"><svg><use href="#i-share"/></svg></a><a href="#" aria-label="Website"><svg><use href="#i-link"/></svg></a><a href="#" aria-label="Email"><svg><use href="#i-mail"/></svg></a><a href="#" aria-label="Profile"><svg><use href="#i-globe"/></svg></a></div></div>
  <a href="#" class="pager" style="left:627px" aria-label="Previous"><svg width="8" height="10"><path d="M6 1L2 5l4 4" stroke="#fff" stroke-width="1.5" fill="none"/></svg></a>
  <a href="#" class="pager pager--on" style="left:661px" aria-label="Next"><svg width="8" height="10"><path d="M2 1l4 4-4 4" stroke="#fff" stroke-width="1.5" fill="none"/></svg></a>
</section>

<h2 class="section-title heroes-title">UNSUNG HEROS</h2>
<div class="heroes-clip">
  <div class="abs arc" role="img" aria-label="Darkened auditorium with audience"></div>
</div>
<a href="#" class="arrow" style="left:180px" aria-label="Previous">←</a>
<a href="#" class="arrow arrow--next" style="left:992px" aria-label="Next">→</a>
<div class="hero-card hero-card--featured" style="left:236px"><span class="mic"></span><div class="pic" role="img" aria-label="Audience member portrait"></div><h5>UNSUNG HERO</h5><small>Asked Question?</small></div>
<div class="hero-card" style="left:388px"><span class="mic"></span><div class="pic" role="img" aria-label="Audience member portrait"></div><h5>UNSUNG HERO</h5><small>Asked Question?</small></div>
<div class="hero-card" style="left:538px"><span class="mic"></span><div class="pic" role="img" aria-label="Audience member portrait"></div><h5>UNSUNG HERO</h5><small>Asked Question?</small></div>
<div class="hero-card" style="left:686px"><span class="mic"></span><div class="pic" role="img" aria-label="Audience member portrait"></div><h5>UNSUNG HERO</h5><small>Asked Question?</small></div>
<div class="hero-card" style="left:836px"><span class="mic"></span><div class="pic" role="img" aria-label="Audience member portrait"></div><h5>UNSUNG HERO</h5><small>Asked Question?</small></div>

<section class="abs dorian"></section>
<h2 class="section-title dorian-title">YOU &amp; DORIAN FLECK</h2>
<h3 class="dorian-head">DORIAN FLECK IS A FAMOUS ACTOR WHO MADE THE TERM ‘SIX DEGREES OF SEPARATION’ VERY POPULAR</h3>
<p class="dorian-copy">Ut enim ad minima veniam, quis nostrum exercitationem ullam corporis suscipit laboriosam, nisi ut aliquid ex ea commodi consequatur? Quis autem vel eum iure reprehenderit qui in ea voluptate velit esse quam nihil molestiae consequatur, vel illum qui dolorem eum fugiat quo voluptas nulla pariatur.</p>
<div class="abs video" role="img" aria-label="Black and white portrait video still of the actor"></div>
<div class="play play--video"></div>

<h2 class="section-title partner-title">OUR PARTNER</h2>
<p class="lede partner-lede">Nemo enim ipsam voluptatem quia voluptas sit aspernatur aut odit aut fugit, sed quia consequuntur magni dolores eos qui ratione voluptatem sequi nesciunt.</p>
<a href="#" class="nav-btn nav-btn--prev" aria-label="Previous"><svg width="8" height="12"><path d="M6 1L1 6l5 5" stroke="#fff" stroke-width="2" fill="none"/></svg></a>
<a href="#" class="nav-btn nav-btn--next" aria-label="Next"><svg width="8" height="12"><path d="M2 1l5 5-5 5" stroke="#333" stroke-width="2" fill="none"/></svg></a>
<div class="partner" style="left:236px">PARTNER 1</div>
<div class="partner" style="left:388px">PARTNER 2</div>
<div class="partner" style="left:538px">PARTNER 3</div>
<div class="partner" style="left:688px">PARTNER 4</div>
<div class="partner" style="left:837px">PARTNER 5</div>

<section class="abs contact"></section>
<h2 class="section-title section-title--light contact-title">GET IN TOUCH</h2>
<p class="lede lede--light contact-lede">Nemo enim ipsam voluptatem quia voluptas sit aspernatur aut odit aut fugit, sed quia consequuntur magni dolores eos qui ratione voluptatem sequi nesciunt.</p>
<div class="field" style="top:3027px">Name</div>
<div class="field" style="top:3064px">Email</div>
<div class="field" style="top:3101px">Phone</div>
<div class="field field--message" style="top:3027px">Message</div>
<a href="#" class="send">SEND</a>

<h2 class="section-title section-title--plain connect-title">CONNECT WITH US</h2>
<p class="abs connect-sub">FOLLOW US ON SOCIAL NETWORKS</p>
<div class="abs follow">
  <a href="#" aria-label="Share"><svg viewBox="0 0 24 24"><use href="#i-share"/></svg></a>
  <a href="#" aria-label="Website"><svg viewBox="0 0 24 24"><use href="#i-link"/></svg></a>
  <a href="#" aria-label="Email"><svg viewBox="0 0 24 24"><use href="#i-mail"/></svg></a>
  <a href="#" aria-label="Profile"><svg viewBox="0 0 24 24"><use href="#i-globe"/></svg></a>
</div>
<p class="abs copyright">© 2019 Lumen Harbor Media. All rights reserved.</p>

</body>
</html>
```